Buch-/eBook-Cover für ein Fantasy Roman
Zielgruppe
Meine Zielgruppe sind Jugendliche und junge Erwachsene, aber auch für Ältere könnte mein Buch interessant sein.
Aufgabenstellung
Bei meinem Buch handelt es sich um einen Fantasy Roman. Es heißt 'Nachtfalter - Wahrheit braucht ihre Zeit' und der Autor ist Mara Oswaldtinger.
Das Buch handelt von einem Mädchen, welches eigentlich ein ganz normales Leben führt, aber dieses durch eine Pressekonferenz vom Präsidenten komplett durcheinander gerät. Denn viele Menschen sollen an einem Virus leiden. Die Menschen sollen sich aber keine Sorgen machen. Doch alles läuft durcheinander, da die infizierten Menschen einer nach dem anderen spurlos verschwinden.
Auf meinem Cover soll keine Figur zu sehen sein. Ich hätte gerne ein Zusammenspiel zwischen den Farben Blau und Grün. sie sollen harmonisch und fließend ineinander übergehen. Auch etwas Glitzer für etwas Geheimnisvolles darf auf dem Cover sein. Den Titel hätte ich gerne in der Mitte. Wo der Autorname stehen soll, bin ich offen.

```html
<!DOCTYPE html>
<html lang="de">
<head>
<meta charset="utf-8">
<title>Nachtfalter – Wahrheit braucht ihre Zeit</title>
<link rel="stylesheet" href="https://fonts.googleapis.com/css2?family=Pinyon+Script&family=Barlow:wght@400&display=swap">
<style>
  :root {
    --night: #0b1544;
    --deep-violet: #1d1858;
    --ink-blue: #143f93;
    --azure: #1c62b4;
    --teal: #1e8c8a;
    --lagoon: #2aa7a0;
    --gold: #e2b93b;
    --gold-light: #f3d774;
    --mist: #a7b3cc;
    --frame: #2f8a96;
  }
  html, body {
    margin: 0;
    padding: 0;
    width: 884px;
    height: 1200px;
    overflow: hidden;
    background: var(--night);
  }
  .cover {
    position: relative;
    width: 884px;
    height: 1200px;
    overflow: hidden;
    font-family: "Barlow", sans-serif;
  }
  .cover__sky {
    position: absolute;
    inset: 0;
    background:
      radial-gradient(ellipse 420px 360px at 640px 380px, rgba(42,167,160,0.85), transparent 70%),
      radial-gradient(ellipse 380px 300px at 560px 600px, rgba(28,98,180,0.75), transparent 70%),
      radial-gradient(ellipse 300px 260px at 740px 120px, rgba(30,140,138,0.55), transparent 70%),
      radial-gradient(ellipse 360px 300px at 220px 960px, rgba(20,63,147,0.6), transparent 70%),
      radial-gradient(ellipse 420px 360px at 120px 260px, rgba(29,24,88,0.8), transparent 70%),
      radial-gradient(ellipse 420px 320px at 760px 1080px, rgba(29,24,88,0.7), transparent 70%),
      linear-gradient(160deg, var(--deep-violet), var(--night) 45%, var(--ink-blue) 100%);
  }
  .cover__corner {
    position: absolute;
    width: 190px;
    height: 190px;
  }
  .cover__corner--tl { left: 26px; top: 26px; background: radial-gradient(circle at 0 0, rgba(47,138,150,0.35), transparent 70%); }
  .cover__corner--tr { right: 26px; top: 26px; background: radial-gradient(circle at 100% 0, rgba(47,138,150,0.35), transparent 70%); }
  .cover__corner--bl { left: 26px; bottom: 26px; background: radial-gradient(circle at 0 100%, rgba(47,138,150,0.35), transparent 70%); }
  .cover__corner--br { right: 26px; bottom: 26px; background: radial-gradient(circle at 100% 100%, rgba(47,138,150,0.35), transparent 70%); }
  .cover__frame {
    position: absolute;
    inset: 0;
    pointer-events: none;
  }
  .cover__genre {
    position: absolute;
    top: 204px;
    left: 0;
    right: 0;
    text-align: center;
    font-size: 23px;
    letter-spacing: 1px;
    color: var(--mist);
    text-transform: uppercase;
  }
  .cover__title {
    position: absolute;
    top: 390px;
    left: 0;
    right: 0;
    margin: 0;
    text-align: center;
    font-family: "Pinyon Script", cursive;
    font-weight: 400;
    font-size: 150px;
    line-height: 1;
    color: var(--gold);
    background: linear-gradient(180deg, var(--gold-light), var(--gold) 60%, #c99a26);
    -webkit-background-clip: text;
    background-clip: text;
    -webkit-text-fill-color: transparent;
  }
  .cover__subtitle {
    position: absolute;
    top: 650px;
    left: 0;
    right: 0;
    margin: 0;
    text-align: center;
    font-family: "Pinyon Script", cursive;
    font-size: 60px;
    line-height: 62px;
    color: var(--gold);
  }
  .cover__subtitle span { display: block; }
  .cover__sprig {
    position: absolute;
    left: 412px;
    top: 906px;
    width: 60px;
    height: 40px;
    border-radius: 50%;
    background: radial-gradient(ellipse, rgba(255,255,255,0.7), transparent 70%);
  }
  .cover__author {
    position: absolute;
    top: 1046px;
    left: 0;
    right: 0;
    text-align: center;
    font-size: 27px;
    letter-spacing: 1px;
    color: var(--mist);
    text-transform: uppercase;
  }
</style>
</head>
<body>
  <main class="cover">
    <div class="cover__sky" role="img" aria-label="Sternenhimmel mit blau-grünem Nebel und Glitzer"></div>

    <div class="cover__corner cover__corner--tl" role="img" aria-label="Verschnörkeltes Eckornament"></div>
    <div class="cover__corner cover__corner--tr" role="img" aria-label="Verschnörkeltes Eckornament"></div>
    <div class="cover__corner cover__corner--bl" role="img" aria-label="Verschnörkeltes Eckornament"></div>
    <div class="cover__corner cover__corner--br" role="img" aria-label="Verschnörkeltes Eckornament"></div>

    <svg class="cover__frame" width="884" height="1200" viewBox="0 0 884 1200" aria-hidden="true">
      <g fill="none" stroke="var(--frame)" stroke-width="2.5" opacity="0.8">
        <path d="M48 200 V48 H280"/>
        <path d="M604 48 H836 V200"/>
        <path d="M48 1000 V1152 H280"/>
        <path d="M604 1152 H836 V1000"/>
      </g>
    </svg>

    <p class="cover__genre">Fantasy Roman</p>
    <h1 class="cover__title">Nachtfalter</h1>
    <p class="cover__subtitle">
      <span>Wahrheit braucht</span>
      <span>—ihre Zeit—</span>
    </p>
    <div class="cover__sprig" role="img" aria-label="Kleines weißes Zweig-Ornament"></div>
    <p class="cover__author">Mara Oswaldtinger</p>
  </main>
</body>
</html>
```